Meridale Bidding Collective Website

We are an food equipment auction company and are in need of an updated website. Old website found here: http://meridalebiddingcollective.example/ . We need to be able to share upcoming auctions, past auctions, companies we've worked with, needs to be mobile friendly. We will also need an easy to access back office where we can add new info, auction info, etc.

Target Market(s)

Equipment auctions, large food manufacturers, equipment resalers

Industry/Entity Type

Auction

Coding

Coded - Design and coding required

Number of Pages Required

5+ page

Font styles to use
Sans Serif

Colors
acd136
ffffff

Requirements
Must have
• Back office where we can add new auctions
-mobile friendly
-contact us page,
-services page
-social media widgets
-must match our current logo
-current auctions on front page
- join mailing list
- past auctions / current auctions pages
Nice to have
• Would like it to be clean design, easy to view and find options, modern

```html
<!DOCTYPE html>
<html lang="en">
<head>
<meta charset="utf-8">
<title>Meridale Bidding Collective</title>
<link href="https://fonts.googleapis.com/css2?family=Montserrat:wght@500;600;700&family=Open+Sans:wght@400;600;700&display=swap" rel="stylesheet">
<style>
:root{
  --green:#8dc641;
  --green-dark:#76ad2c;
  --ink:#222;
  --text:#555;
  --muted:#888;
  --topbar:#2b2b2b;
  --footer:#0c0c0c;
  --light:#f4f4f4;
  --red:#d9262b;
  --white:#fff;
}
*{box-sizing:border-box;margin:0;padding:0}
html,body{width:1200px;height:3572px;overflow:hidden}
body{font-family:"Open Sans",Arial,sans-serif;color:var(--text);background:var(--white);font-size:14px}
h1,h2,h3,h4{font-family:"Montserrat",Arial,sans-serif}
.topbar{height:32px;background:var(--topbar);color:#ddd;font-size:12px;display:flex;align-items:center;padding:0 52px;gap:8px}
.topbar .dot{width:10px;height:10px;border-radius:50%;background:var(--green)}
.header{height:120px;display:flex;align-items:center;padding:0 76px;justify-content:space-between}
.brand{display:flex;align-items:center;gap:12px}
.brand-mark{width:44px;height:44px;background:var(--green)}
.brand-name{font-family:"Montserrat",sans-serif;font-weight:700;font-size:19px;line-height:1.1;color:var(--ink);width:190px}
.subscribe{display:flex;align-items:center}
.subscribe .field{width:290px;height:38px;border:1px solid #ccc;border-radius:20px 0 0 20px;padding:0 16px;font-size:12px;color:#999;display:flex;align-items:center}
.subscribe .btn{height:38px;padding:0 24px;background:var(--green);color:#fff;font-weight:700;font-size:12px;border-radius:0 20px 20px 0;display:flex;align-items:center;margin-left:-14px}
.call{display:flex;align-items:center;gap:10px}
.call .icon{width:38px;height:38px;border-radius:50%;background:var(--green);display:flex;align-items:center;justify-content:center}
.call small{display:block;font-size:10px;color:var(--muted);text-transform:uppercase;letter-spacing:1px}
.call strong{font-family:"Montserrat",sans-serif;font-size:22px;color:var(--ink)}
.nav{height:36px;background:var(--green);display:flex;align-items:center;padding:0 200px;gap:0}
.nav a{color:#fff;font-size:12px;font-weight:700;text-decoration:none;padding:0 20px;height:36px;display:flex;align-items:center}
.nav a.active{background:var(--green-dark)}
.hero{position:relative;height:580px;background:linear-gradient(180deg,#5c6468,#3d4448 60%,#2f3437);display:flex;flex-direction:column;align-items:center;justify-content:center;text-align:center;color:#fff}
.hero-badge{width:56px;height:56px;border:2px solid #fff;transform:rotate(45deg);margin-bottom:40px}
.hero h1{font-size:40px;font-weight:600;line-height:1.25;text-transform:uppercase;max-width:900px}
.btn-pill{display:inline-block;background:var(--green);color:#fff;font-weight:700;font-size:13px;padding:12px 34px;border-radius:24px;text-transform:uppercase}
.hero .btn-pill{margin-top:36px}
.hero-dots{position:absolute;bottom:28px;display:flex;gap:8px}
.hero-dots span{width:8px;height:8px;border-radius:50%;background:rgba(255,255,255,.5)}
.hero-dots span.on{background:#fff}
.welcome{height:552px;background:var(--light);display:flex;align-items:center;padding:0 120px;gap:110px}
.welcome-art{width:340px;height:340px;background:linear-gradient(135deg,#b9d98c,#7f9f88);flex:none}
.welcome-copy{width:500px}
.welcome h2{font-size:34px;font-weight:700;color:var(--ink);line-height:1.15;text-transform:uppercase;margin-bottom:12px}
.accent{color:var(--green)}
.rule{width:70px;height:3px;background:var(--green);margin-bottom:22px}
.welcome p{font-size:14px;line-height:1.8;margin-bottom:26px}
.services{height:800px;text-align:center;padding-top:70px}
.section-title{font-size:34px;font-weight:700;color:var(--ink);text-transform:uppercase}
.section-sub{font-size:12px;font-weight:700;color:var(--ink);text-transform:uppercase;margin:20px 0 40px;letter-spacing:.5px}
.center-rule{width:60px;height:3px;background:var(--green);margin:10px auto 0}
.service-grid{display:grid;grid-template-columns:repeat(3,300px);justify-content:center;column-gap:70px;row-gap:50px}
.service svg{display:block;margin:0 auto 16px}
.service h3{font-size:14px;font-weight:700;color:var(--ink);text-transform:uppercase;margin-bottom:12px;padding-bottom:10px;border-bottom:1px solid #ddd}
.service p{font-size:13px;line-height:1.7}
.partners{height:320px;background:var(--green);text-align:center;padding-top:60px}
.partners .section-title{color:#fff}
.partner-row{display:flex;justify-content:center;gap:24px;margin-top:50px}
.partner-row span{width:150px;height:82px;background:#fff}
.auctions{height:900px;text-align:center;padding-top:96px}
.tabs{display:flex;justify-content:center;gap:30px;margin:40px 0 38px;font-size:12px;font-weight:700;text-transform:uppercase;color:var(--ink)}
.tabs .on{color:var(--green)}
.card-grid{display:grid;grid-template-columns:repeat(2,480px);justify-content:center;gap:26px 40px;text-align:left}
.card{position:relative;height:290px;background:#fff;box-shadow:0 4px 18px rgba(0,0,0,.12);display:flex}
.card-photo{width:220px;height:100%;flex:none}
.card-body{padding:22px 24px;flex:1}
.card h4{font-size:16px;font-weight:700;color:var(--ink);line-height:1.35;text-transform:uppercase;margin-bottom:14px}
.card .meta{font-size:12px;color:var(--green);font-weight:600;text-transform:uppercase}
.card .place{font-size:12px;color:var(--muted);margin:4px 0 26px}
.card .more{font-size:12px;font-weight:700;color:var(--green);text-transform:uppercase}
.card .badge{position:absolute;right:16px;bottom:18px;width:50px;height:50px;border-radius:50%;background:var(--red);color:#fff;font-size:9px;font-weight:700;display:flex;align-items:center;justify-content:center;text-align:center;line-height:1.1}
.footer{height:232px;background:var(--footer);color:#ccc;padding:46px 76px 0;position:relative}
.footer-cols{display:flex}
.footer-brand{width:340px}
.footer-brand .brand-name{color:#fff}
.socials{display:flex;gap:10px;margin-top:30px}
.socials span{width:28px;height:28px;border-radius:50%;background:var(--green)}
.footer-col{width:180px;font-size:12px;line-height:1.9}
.footer-col.wide{width:auto;margin-left:40px}
.footer-col h4{font-size:13px;color:#fff;text-transform:uppercase;margin-bottom:8px}
.copyright{position:absolute;left:0;right:0;bottom:14px;text-align:center;font-size:11px;color:#999}
</style>
</head>
<body>
<div class="topbar"><span class="dot"></span>hello@meridalebidding.example</div>

<header class="header">
  <div class="brand"><span class="brand-mark"></span><span class="brand-name">Meridale Bidding Collective</span></div>
  <div class="subscribe"><span class="field">Enter Your Email</span><span class="btn">SUBSCRIBE</span></div>
  <div class="call">
    <span class="icon"><svg width="18" height="18" viewBox="0 0 24 24"><path fill="#fff" d="M6.6 10.8a15 15 0 0 0 6.6 6.6l2.2-2.2a1 1 0 0 1 1-.25 11.4 11.4 0 0 0 3.6.6 1 1 0 0 1 1 1V20a1 1 0 0 1-1 1A17 17 0 0 1 3 4a1 1 0 0 1 1-1h3.5a1 1 0 0 1 1 1c0 1.25.2 2.45.6 3.6a1 1 0 0 1-.25 1z"/></svg></span>
    <div><small>Call Today</small><strong>(555) 204-7781</strong></div>
  </div>
</header>

<nav class="nav">
  <a class="active">HOME</a><a>ABOUT US</a><a>SERVICES</a><a>PAST</a><a>AUCTIONS</a><a>EQUIPMENT FINDER</a><a>CONTACT US</a>
</nav>

<section class="hero" role="img" aria-label="Food manufacturing plant with packaging equipment lines">
  <div class="hero-badge"></div>
  <h1>Leaders in Food Manufacturing and Packaging Equipment Auctions</h1>
  <span class="btn-pill">Get Started</span>
  <div class="hero-dots"><span class="on"></span><span></span><span></span><span></span></div>
</section>

<section class="welcome">
  <div class="welcome-art" role="img" aria-label="Large brand emblem area"></div>
  <div class="welcome-copy">
    <h2>Welcome Meridale <span class="accent">Bidding Collective</span></h2>
    <div class="rule"></div>
    <p>Meridale Bidding Collective is a full-service asset management company specializing in food manufacturing and packaging equipment. Our goal at Meridale Bidding Collective is to provide our customers with a range of options to liquidate their assets. A few of the services we offer are appraisals, asset management, live onsite auctions, online auctions and orderly negotiated sales. We help our customers determine the best options to maximize returns within their given parameters.</p>
    <span class="btn-pill">Learn More</span>
  </div>
</section>

<section class="services">
  <h2 class="section-title">Our <span class="accent">Services</span></h2>
  <div class="center-rule"></div>
  <p class="section-sub">Below are a list of our services please contact us for more information.</p>
  <div class="service-grid">
    <div class="service">
      <svg width="76" height="84" viewBox="0 0 76 84"><polygon points="38,2 74,22 74,62 38,82 2,62 2,22" fill="var(--green)"/><path d="M26 42l9 9 16-18" stroke="#fff" stroke-width="4" fill="none"/></svg>
      <h3>Appraisals</h3><p>Lorem ipsum dolor sit amet, consectetur adipiscing elit, sed do eiusmod tempor incididunt.</p>
    </div>
    <div class="service">
      <svg width="76" height="84" viewBox="0 0 76 84"><polygon points="38,2 74,22 74,62 38,82 2,62 2,22" fill="var(--green)"/><rect x="24" y="44" width="6" height="12" fill="#fff"/><rect x="35" y="36" width="6" height="20" fill="#fff"/><rect x="46" y="28" width="6" height="28" fill="#fff"/></svg>
      <h3>Asset Management</h3><p>Lorem ipsum dolor sit amet, consectetur adipiscing elit, sed do eiusmod tempor incididunt.</p>
    </div>
    <div class="service">
      <svg width="76" height="84" viewBox="0 0 76 84"><polygon points="38,2 74,22 74,62 38,82 2,62 2,22" fill="var(--green)"/><rect x="26" y="30" width="22" height="10" transform="rotate(-40 37 35)" fill="#fff"/><rect x="36" y="40" width="4" height="18" transform="rotate(-40 38 49)" fill="#fff"/><rect x="24" y="56" width="22" height="4" fill="#fff"/></svg>
      <h3>Auctions</h3><p>Lorem ipsum dolor sit amet, consectetur adipiscing elit, sed do eiusmod tempor incididunt.</p>
    </div>
    <div class="service">
      <svg width="76" height="84" viewBox="0 0 76 84"><polygon points="38,2 74,22 74,62 38,82 2,62 2,22" fill="var(--green)"/><circle cx="38" cy="42" r="13" stroke="#fff" stroke-width="4" fill="none"/><circle cx="38" cy="42" r="4" fill="#fff"/></svg>
      <h3>Turnkey Operations</h3><p>Lorem ipsum dolor sit amet, consectetur adipiscing elit, sed do eiusmod tempor incididunt.</p>
    </div>
    <div class="service">
      <svg width="76" height="84" viewBox="0 0 76 84"><polygon points="38,2 74,22 74,62 38,82 2,62 2,22" fill="var(--green)"/><path d="M24 42l14-12 14 12v14H24z" fill="#fff"/><rect x="34" y="46" width="8" height="10" fill="var(--green)"/></svg>
      <h3>Real Estate</h3><p>Lorem ipsum dolor sit amet, consectetur adipiscing elit, sed do eiusmod tempor incididunt.</p>
    </div>
    <div class="service">
      <svg width="76" height="84" viewBox="0 0 76 84"><polygon points="38,2 74,22 74,62 38,82 2,62 2,22" fill="var(--green)"/><rect x="26" y="28" width="24" height="30" rx="2" fill="#fff"/><path d="M31 37h14M31 43h14M31 49h9" stroke="var(--green)" stroke-width="3"/></svg>
      <h3>Orderly Negotiated Sales</h3><p>Lorem ipsum dolor sit amet, consectetur adipiscing elit, sed do eiusmod tempor incididunt.</p>
    </div>
  </div>
</section>

<section class="partners">
  <h2 class="section-title">Companies We've Worked With</h2>
  <div class="partner-row"><span></span><span></span><span></span><span></span><span></span><span></span></div>
</section>

<section class="auctions">
  <h2 class="section-title">Our Upcoming &amp; <span class="accent">Past Auctions</span></h2>
  <div class="center-rule"></div>
  <div class="tabs"><span>All</span><span>|</span><span>Upcoming Auctions</span><span>|</span><span class="on">Past Auctions</span></div>
  <div class="card-grid">
    <article class="card">
      <div class="card-photo" role="img" aria-label="Dessert production line equipment" style="background:linear-gradient(160deg,#a4a7a2,#6f6a60)"></div>
      <div class="card-body"><h4>Surplus Assets to National Premium Dessert Supplier and Bakery Producer</h4><p class="meta">6/30/2020 10:00 AM</p><p class="place">Multi Location California &amp; Oregon</p><span class="more">View Details</span></div>
      <span class="badge">AUCTION<br>CLOSED</span>
    </article>
    <article class="card">
      <div class="card-photo" role="img" aria-label="Candy and confection conveyor line" style="background:linear-gradient(160deg,#9a7b63,#5b4a3c)"></div>
      <div class="card-body"><h4>Large Candy &amp; Confections Surplus Equipment Auction</h4><p class="meta">6/25/2020 10:00 AM</p><p class="place">Northfield, OH</p><span class="more">View Details</span></div>
      <span class="badge">AUCTION<br>CLOSED</span>
    </article>
    <article class="card">
      <div class="card-photo" role="img" aria-label="Bakery bun and pastry production equipment" style="background:linear-gradient(160deg,#b7b3ab,#77726a)"></div>
      <div class="card-body"><h4>Major Bakery Closure : Buns, Baguettes, Pies &amp; Pastries</h4><p class="meta">6/18/2020 10:00 AM</p><p class="place">Westbrook, MA</p><span class="more">View Details</span></div>
      <span class="badge">AUCTION<br>CLOSED</span>
    </article>
    <article class="card">
      <div class="card-photo" role="img" aria-label="Donut manufacturing machinery" style="background:linear-gradient(160deg,#a9aeb0,#6c7275)"></div>
      <div class="card-body"><h4>Former Assets of a Major Bakery &amp; Donut Manufacturer</h4><p class="meta">6/10/2020 10:00 AM</p><p class="place">Multi Location California &amp; Oregon</p><span class="more">View Details</span></div>
      <span class="badge">AUCTION<br>CLOSED</span>
    </article>
  </div>
</section>

<footer class="footer">
  <div class="footer-cols">
    <div class="footer-brand">
      <div class="brand"><span class="brand-mark"></span><span class="brand-name">Meridale Bidding Collective</span></div>
      <div class="socials"><span></span><span></span><span></span><span></span></div>
    </div>
    <div class="footer-col"><h4>Quick Links</h4>› Home<br>› About Us<br>› Services<br>› Auctions<br>› Equipment Finder</div>
    <div class="footer-col"><h4>Legal</h4>› Terms of Use<br>› Privacy Policy<br>› Contact Us<br>› FAQ</div>
    <div class="footer-col wide"><h4>Contact Us</h4>Meridale Bidding Collective<br>48 Harrow Lane<br>Fenwick, ND 58000<br>(555) 204-7781<br>hello@meridalebidding.example</div>
  </div>
  <p class="copyright">© Copyrights 2020. Meridale Bidding Collective &nbsp;|&nbsp; All Rights Reserved</p>
</footer>
</body>
</html>
```